Communication Business Card Design

We offer complete cabling solutions
Data Cabling,Fibre Optic, and Cabling Repairs fault finding
Security camera installation
TV Aerial installation
Security alarm installation
HWR

Industry/Entity Type

Business

Contact Information for Business Card

Brightmoor Solutions
ABN 58 214 992 367
EMAIL brightmoorsolutions.com.au
Mobile 0491236057
Lou Archer

```html
<!DOCTYPE html>
<html lang="en">
<head>
<meta charset="utf-8">
<title>Brightmoor Solutions – Business Card</title>
<link href="https://fonts.googleapis.com/css2?family=Arimo:wght@400;700&display=swap" rel="stylesheet">
<style>
  :root {
    --stage: #1b2426;
    --sky: #1eb4ec;
    --sky-light: #3fd5f8;
    --ink-grey: #6b6d70;
    --night: #111213;
    --paper: #ffffff;
    --accent: #29b6e8;
  }
  * { box-sizing: border-box; margin: 0; padding: 0; }
  html, body {
    width: 1200px; height: 800px; overflow: hidden;
    background: var(--stage);
    font-family: "Arimo", Arial, sans-serif;
  }
  .canvas { position: relative; width: 1200px; height: 800px; }

  .card {
    position: absolute; top: 245px;
    width: 540px; height: 310px;
    overflow: hidden;
    box-shadow: 0 14px 34px rgba(0,0,0,.45);
  }

  /* Front */
  .card--front {
    left: 40px;
    background: linear-gradient(120deg, var(--sky) 0%, var(--sky-light) 100%);
  }
  .card--front .brand {
    position: absolute; left: 0; right: 0; top: 112px;
    text-align: center;
    font-size: 40px; font-weight: 700; color: var(--ink-grey);
    letter-spacing: -0.5px;
  }
  .card--front .tagline-band {
    position: absolute; left: 0; right: 0; bottom: 38px; height: 44px;
    background: var(--paper);
    display: flex; align-items: center; justify-content: center;
  }
  .card--front .tagline {
    font-size: 15px; font-weight: 700; color: var(--accent);
    letter-spacing: 3px; text-transform: uppercase;
  }

  /* Back */
  .card--back {
    left: 620px;
    background: var(--night);
    display: flex;
  }
  .card--back .brand-panel {
    width: 210px; height: 100%;
    background: linear-gradient(160deg, var(--sky-light) 0%, var(--sky) 100%);
    padding: 40px 18px 0 18px;
  }
  .card--back .brand {
    font-size: 22px; font-weight: 700; color: var(--ink-grey);
    text-align: right; line-height: 1.1;
  }
  .card--back .details {
    flex: 1; padding: 30px 26px 22px 28px;
    color: var(--paper);
    display: flex; flex-direction: column;
  }
  .person-name {
    font-size: 21px; font-weight: 700; color: var(--accent);
    text-transform: uppercase; letter-spacing: .5px;
  }
  .person-role { font-size: 17px; margin-top: 2px; }
  .services { list-style: none; margin-top: 18px; font-size: 15px; line-height: 1.3; }
  .services li::before { content: "- "; }
  .contact { margin-top: auto; font-size: 12px; line-height: 1.7; }
  .contact-row { display: flex; align-items: center; gap: 6px; }
  .contact svg { width: 11px; height: 11px; fill: var(--accent); flex: none; }
  .contact .divider { color: var(--accent); margin: 0 4px; }
</style>
</head>
<body>
<main class="canvas">

  <section class="card card--front" aria-label="Business card front">
    <div class="brand">Brightmoor Solutions</div>
    <div class="tagline-band">
      <span class="tagline">Your complete cabling solutions</span>
    </div>
  </section>

  <section class="card card--back" aria-label="Business card back">
    <div class="brand-panel">
      <div class="brand">Brightmoor Solutions</div>
    </div>
    <div class="details">
      <div class="person-name">Lou Archer</div>
      <div class="person-role">Manager</div>
      <ul class="services">
        <li>Data Cabling</li>
        <li>Fibre Optic</li>
        <li>Cabling Repairs</li>
        <li>Security camera installation</li>
        <li>TV Aerial installation</li>
        <li>Security alarm installation</li>
        <li>HWR</li>
      </ul>
      <div class="contact">
        <div class="contact-row">
          <svg viewBox="0 0 12 12" aria-hidden="true"><path d="M4 0h1.4l-.4 3h2.2l.4-3H9l-.4 3H11v1.4H8.4L8.1 7.6H10.6V9H7.9l-.4 3H6.1l.4-3H4.3l-.4 3H2.5l.4-3H.4V7.6h2.7l.3-3.2H1V3h2.6z M4.8 4.4l-.3 3.2h2.2l.3-3.2z"/></svg>
          <span>ABN 58 214 992 367</span>
          <span class="divider">|</span>
          <svg viewBox="0 0 12 12" aria-hidden="true"><path d="M2.4 0.6l2 2.4-1.1 1.3c.7 1.6 2 2.9 3.6 3.6l1.3-1.1 2.4 2-1.3 2.3C4.5 11 1 7.5.1 2z"/></svg>
          <span>0491236057</span>
        </div>
        <div class="contact-row">
          <svg viewBox="0 0 12 12" aria-hidden="true"><path d="M0 2h12v8H0z M1 3v.3l5 3.2 5-3.2V3z" fill-rule="evenodd"/></svg>
          <span>email@brightmoorsolutions.com.au</span>
        </div>
      </div>
    </div>
  </section>

</main>
</body>
</html>
```